Bramble Peak Information Technology Business Card
Services for Move Add Change, Technical Relocation, Server Room Support, Technical Support
Bramble Peak Information Technology Business Card - Information Technology
Creative Brief
Professional
Owen Darlisk
2917 41st Lane Northeast Seattle WA 98422
owen@bramblepkit-example.com
www.bramblepkit-example.com
The original logo on the back, #34 and #35
Move Add and Changes, Corporate Relocation, Server Room Support, Technical Support

```html
<!DOCTYPE html>
<html lang="en">
<head>
<meta charset="utf-8">
<title>Bramble Peak Information Technology – Stationery</title>
<link href="https://fonts.googleapis.com/css2?family=Montserrat:wght@400;600;800&display=swap" rel="stylesheet">
<style>
:root{
  --bg:#eceeef;
  --paper:#ffffff;
  --charcoal:#3a3a3a;
  --orange:#f7941d;
  --ink:#555555;
  --soft:#8a8a8a;
  --light:#f2f2f2;
}
*{box-sizing:border-box;margin:0;padding:0}
html,body{width:1200px;height:937px;overflow:hidden}
body{background:var(--bg);position:relative;font-family:'Montserrat',Arial,sans-serif;color:var(--ink)}
.piece{position:absolute;background:var(--paper);overflow:hidden}
.wave{position:absolute;left:0;bottom:0;width:100%}
.wave .band{fill:var(--charcoal)}
.wave .swoosh{fill:var(--orange)}
.brand{position:absolute;display:flex;align-items:center;gap:.3em;font-weight:800;color:var(--charcoal);letter-spacing:.02em;white-space:nowrap}
.brand .dot{width:.55em;height:.55em;border-radius:50%;background:var(--orange)}
.url{position:absolute;color:#fff;font-weight:600;letter-spacing:.12em;white-space:nowrap}

/* letterhead */
.letterhead{left:71px;top:63px;width:506px;height:557px}
.letterhead .brand{left:26px;top:26px;font-size:22px}
.letter{position:absolute;left:26px;top:92px;width:440px;font-size:6px;line-height:1.55;color:var(--soft)}
.letter p{margin-bottom:9px}
.signature{height:22px;width:60px;border-bottom:1px solid var(--soft);margin-bottom:6px}
.letterhead .wave{height:150px}
.letter-contact{position:absolute;right:26px;bottom:14px;text-align:right;color:#fff;font-size:6.5px;line-height:1.6}

/* folder */
.folder{left:633px;top:38px;width:549px;height:590px}
.folder .brand{left:50%;top:220px;transform:translateX(-50%);font-size:46px}
.folder .wave{height:170px}
.folder .url{right:26px;bottom:20px;font-size:11px}

/* business cards */
.card-front{left:46px;top:653px;width:207px;height:114px}
.card-front .brand{left:10px;top:14px;font-size:12px}
.card-front .tag{position:absolute;right:10px;top:12px;font-size:5px;font-weight:600;color:var(--orange);text-align:right;line-height:1.5}
.card-front .details{position:absolute;right:10px;top:34px;font-size:4.6px;line-height:1.6;text-align:right;color:var(--ink)}
.card-front .wave{height:40px}
.card-back{left:46px;top:785px;width:207px;height:119px}
.card-back .brand{left:50%;top:50%;transform:translate(-50%,-50%);font-size:14px}

/* envelope front */
.envelope{left:266px;top:668px;width:456px;height:213px}
.envelope .brand{left:20px;top:20px;font-size:18px}
.envelope .wave{height:110px}
.envelope .url{right:24px;bottom:14px;font-size:8.5px}

/* envelope back */
.envelope-back{left:737px;top:673px;width:443px;height:211px}
.envelope-back svg{position:absolute;inset:0;width:100%;height:100%}
.envelope-back .url{left:50%;top:28px;transform:translateX(-50%);font-size:9px}
</style>
</head>
<body>

<section class="piece letterhead">
  <div class="brand">BRAMBLE PEAK<span class="dot"></span></div>
  <div class="letter">
    <p>June 4, 2024<br>Client Name<br>100 Main Street, Seattle WA</p>
    <p>Thank you for choosing our team for your office move. We will plan each step, protect your equipment, and keep your network running from the first box to the last cable.</p>
    <p>Our technicians handle server rooms, desk moves and daily support, so your staff can focus on their work.</p>
    <p>Please call us with any questions. We look forward to working with you.</p>
    <p>Sincerely,</p>
    <div class="signature"></div>
    <p>Owen Darlisk<br>Director<br>2917 41st Lane Northeast</p>
  </div>
  <svg class="wave" viewBox="0 0 100 100" preserveAspectRatio="none" aria-hidden="true">
    <path class="band" d="M0 70 C35 25,65 25,100 10 L100 100 L0 100Z"/>
    <path class="swoosh" d="M0 58 C35 8,65 10,100 0 L100 8 C65 20,35 20,0 66Z"/>
  </svg>
  <div class="letter-contact">
    2917 41st Lane Northeast<br>Seattle WA 98422<br>Phone: 206 555 0142<br>Fax: 206 555 0143<br>owen@bramblepkit-example.com<br>www.bramblepkit-example.com
  </div>
</section>

<section class="piece folder">
  <div class="brand">BRAMBLE PEAK<span class="dot"></span></div>
  <svg class="wave" viewBox="0 0 100 100" preserveAspectRatio="none" aria-hidden="true">
    <path class="band" d="M0 70 C35 25,65 25,100 10 L100 100 L0 100Z"/>
    <path class="swoosh" d="M0 58 C35 8,65 10,100 0 L100 8 C65 20,35 20,0 66Z"/>
  </svg>
  <div class="url">www.bramblepkit-example.com</div>
</section>

<section class="piece card-front">
  <div class="brand">BRAMBLE PEAK<span class="dot"></span></div>
  <div class="tag">Owen Darlisk<br><span style="color:var(--soft);font-weight:400">Director</span></div>
  <div class="details">
    Phone: 206 555 0142<br>owen@bramblepkit-example.com<br>www.bramblepkit-example.com<br>2917 41st Lane Northeast<br>Seattle WA 98422
  </div>
  <svg class="wave" viewBox="0 0 100 100" preserveAspectRatio="none" aria-hidden="true">
    <path class="band" d="M0 70 C35 25,65 25,100 10 L100 100 L0 100Z"/>
    <path class="swoosh" d="M0 58 C35 8,65 10,100 0 L100 8 C65 20,35 20,0 66Z"/>
  </svg>
</section>

<section class="piece card-back">
  <div class="brand">BRAMBLE PEAK<span class="dot"></span></div>
</section>

<section class="piece envelope">
  <div class="brand">BRAMBLE PEAK<span class="dot"></span></div>
  <svg class="wave" viewBox="0 0 100 100" preserveAspectRatio="none" aria-hidden="true">
    <path class="band" d="M0 70 C35 25,65 25,100 10 L100 100 L0 100Z"/>
    <path class="swoosh" d="M0 58 C35 8,65 10,100 0 L100 8 C65 20,35 20,0 66Z"/>
  </svg>
  <div class="url">www.bramblepkit-example.com</div>
</section>

<section class="piece envelope-back">
  <svg viewBox="0 0 100 100" preserveAspectRatio="none" aria-hidden="true">
    <rect x="0" y="0" width="100" height="36" fill="var(--charcoal)"/>
    <path d="M0 36 L50 70 L100 36" fill="none" stroke="#dcdcdc" stroke-width="0.4" vector-effect="non-scaling-stroke"/>
    <path d="M0 100 L44 66 M100 100 L56 66" fill="none" stroke="#e6e6e6" stroke-width="0.4" vector-effect="non-scaling-stroke"/>
  </svg>
  <div class="url">www.bramblepkit-example.com</div>
</section>

</body>
</html>
```